North Fern Holdings Business Card

A business card design to accompany the logo design you completed on Artisan Hive. We are open to your proposals. I did add one idea below that might work, but we aren't married to the idea. The company is a real estate services company. Clientele are typically high net worth individuals, executive level employment or owners of their own company, 30-60 years old.

Our 1 (bad?) idea: double sided card; One side landscape with logo and word mark. Other side Portrait with the logo only (oversize watermark maybe?). Somewhere add text of Name (Marcus Pellington), Title (Principal), phone # (949-555-0173) and email address (marcus@northfernhq.com). There would be a second design with my wife's name, number and email in place of mine.

Again totally open to ideas here.

Industry/Entity Type

Real Estate

```html
<!DOCTYPE html>
<html lang="en">
<head>
<meta charset="utf-8">
<title>North Fern Holdings — Business Card</title>
<link href="https://fonts.googleapis.com/css2?family=Cinzel:wght@400&family=Arimo:wght@400&display=swap" rel="stylesheet">
<style>
  :root {
    --sage: #66955a;
    --sage-light: #7ba56f;
    --paper: #ffffff;
    --watermark: #eceee7;
    --ink: #2f3a2c;
    --stage: #e9e9e9;
  }
  * { box-sizing: border-box; margin: 0; padding: 0; }
  html, body { width: 1200px; height: 1200px; overflow: hidden; }
  body {
    background: var(--stage);
    position: relative;
    font-family: "Arimo", Arial, sans-serif;
  }
  .card {
    position: absolute;
    overflow: hidden;
    box-shadow: 0 6px 18px rgba(0,0,0,0.18);
  }

  /* Front: landscape, sage field with wordmark */
  .card-front {
    left: 83px; top: 423px;
    width: 620px; height: 354px;
    background: var(--sage);
  }
  .card-front .watermark {
    position: absolute; left: -60px; top: -40px;
    width: 420px; height: 440px;
    background: radial-gradient(ellipse at 45% 45%, var(--sage-light) 0%, rgba(123,165,111,0.35) 55%, rgba(123,165,111,0) 72%);
  }
  .wordmark {
    position: absolute; left: 0; right: 0;
    text-align: center;
    font-family: "Cinzel", "Times New Roman", serif;
    font-weight: 400;
  }
  .card-front .mark-dot {
    position: absolute; left: 50%; top: 84px;
    width: 64px; height: 64px; margin-left: -32px;
    border-radius: 50%;
    background: var(--paper);
  }
  .card-front .wordmark { top: 170px; color: var(--paper); }
  .wordmark .line-main { display: block; font-size: 36px; letter-spacing: 1px; line-height: 1.1; }
  .wordmark .line-sub { display: block; font-size: 19px; letter-spacing: 5px; line-height: 1.2; }

  /* Back: portrait, white field with name band */
  .card-back {
    left: 763px; top: 290px;
    width: 354px; height: 620px;
    background: var(--paper);
  }
  .card-back .watermark {
    position: absolute; left: 60px; top: 20px;
    width: 360px; height: 600px;
    background: radial-gradient(ellipse at 55% 40%, var(--watermark) 0%, rgba(236,238,231,0.6) 50%, rgba(236,238,231,0) 72%);
  }
  .card-back .mark-dot {
    position: absolute; left: 50%; top: 80px;
    width: 58px; height: 58px; margin-left: -29px;
    border-radius: 50%;
    background: var(--sage);
  }
  .card-back .wordmark { top: 156px; color: var(--sage); }
  .card-back .wordmark .line-main { font-size: 24px; }
  .card-back .wordmark .line-sub { font-size: 13px; letter-spacing: 4px; }

  .name-band {
    position: absolute; left: 0; right: 0; top: 262px;
    height: 76px;
    background: var(--sage);
    color: var(--paper);
    text-align: center;
    padding-top: 16px;
  }
  .name-band .person { font-size: 21px; line-height: 1.2; }
  .name-band .role { font-size: 14px; line-height: 1.4; opacity: 0.9; }

  .contact {
    position: absolute; left: 48px; top: 372px;
    list-style: none;
    color: var(--ink);
    font-size: 15px;
  }
  .contact li { display: flex; align-items: center; gap: 9px; margin-bottom: 12px; }
  .contact svg { width: 15px; height: 15px; flex: none; }
</style>
</head>
<body>

  <section class="card card-front" aria-label="Card front">
    <div class="watermark" role="img" aria-label="Faint oversized crest watermark"></div>
    <div class="mark-dot"></div>
    <h1 class="wordmark">
      <span class="line-main">North Fern</span>
      <span class="line-sub">Holdings</span>
    </h1>
  </section>

  <section class="card card-back" aria-label="Card back">
    <div class="watermark" role="img" aria-label="Faint oversized crest watermark"></div>
    <div class="mark-dot"></div>
    <h2 class="wordmark">
      <span class="line-main">North Fern</span>
      <span class="line-sub">Holdings</span>
    </h2>
    <div class="name-band">
      <p class="person">Marcus Pellington</p>
      <p class="role">Principal</p>
    </div>
    <ul class="contact">
      <li>
        <svg viewBox="0 0 16 16" aria-hidden="true"><rect width="16" height="16" rx="3" fill="#66955a"/><path d="M5 4.5c.4-.4 1-.4 1.3 0l.8 1c.3.4.2.8-.1 1.1l-.5.5c.5 1 1.3 1.8 2.3 2.3l.5-.5c.3-.3.8-.4 1.1-.1l1 .8c.4.3.4.9 0 1.3l-.6.6c-.6.6-1.6.6-2.5.1A9 9 0 0 1 4.4 8c-.5-.9-.5-1.9.1-2.5z" fill="#fff"/></svg>
        <span>949-555-0173</span>
      </li>
      <li>
        <svg viewBox="0 0 16 16" aria-hidden="true"><rect width="16" height="16" rx="3" fill="#66955a"/><rect x="3.5" y="5" width="9" height="6.5" fill="none" stroke="#fff" stroke-width="1.2"/><path d="M3.5 5 8 8.6 12.5 5" fill="none" stroke="#fff" stroke-width="1.2"/></svg>
        <span>marcus@northfernhq.com</span>
      </li>
    </ul>
  </section>

</body>
</html>
```